Prospective Client Marketing Power Point Refresh/Update

My company has been using the attached power point to share with prospective clients. I'd like to have it refreshed with new graphics and style. The color pallet is something we'd like to stay true to. We are looking for your design expertise and ideas to help us update the look of the PP. We work with high wealth clients and want to have this reflect the value we can bring to the table.

Target Market(s)

Wealth Management Clients

Industry/Entity Type

Financial Advisors

Font styles to use
Sans Serif

Colors
0054AA
0677BA
7BADD7
CADEEF
E8F1F8
0094D4
00A9DD
6FCCEA
C7EBF8
E9F6FB

Requirements
Must have
• Updated look
Nice to have
• Fresh graphics

```html
<!DOCTYPE html>
<html lang="en">
<head>
<meta charset="utf-8">
<title>Harbor Wealth – Brochure Pages</title>
<link href="https://fonts.googleapis.com/css2?family=Montserrat:wght@400;500;700&family=Pinyon+Script&display=swap" rel="stylesheet">
<style>
  :root{
    --blue-deep:#0054AA;
    --blue-mid:#0677BA;
    --blue-soft:#7BADD7;
    --blue-pale:#CADEEF;
    --blue-mist:#E8F1F8;
    --cyan:#0094D4;
    --ink:#1d1d1f;
    --band:#2b2b2d;
    --stage:#2f2f31;
    --label:#ffffff;
    --white:#ffffff;
  }
  *{box-sizing:border-box;margin:0;padding:0}
  html,body{width:1200px;height:2667px;overflow:hidden;background:var(--stage)}
  body{position:relative;font-family:"Montserrat",Arial,sans-serif;color:var(--ink)}

  .page{position:absolute;width:900px;height:508px;overflow:hidden;box-shadow:0 6px 18px rgba(0,0,0,.35)}
  .page-label{position:absolute;color:var(--label);font-size:24px;letter-spacing:12px;white-space:nowrap;transform-origin:left top}

  /* Cover */
  .cover{left:70px;top:300px;background:var(--white)}
  .cover-brand{position:absolute;left:0;right:0;top:56px;text-align:center;font-size:52px;font-weight:700;color:var(--blue-deep);letter-spacing:.5px}
  .cover-photo{position:absolute;left:0;top:150px;width:900px;height:262px;
    background:linear-gradient(180deg,#e9eef2 0%,#b9c4cd 35%,#5d6b78 62%,#2f3a44 78%,#6d5a3c 88%,#8a9aa8 100%)}
  .cover-rule{position:absolute;left:0;top:414px;width:900px;height:4px;background:var(--white)}
  .cover-band{position:absolute;left:0;top:418px;width:900px;height:60px;background:var(--band);
    display:flex;align-items:center;justify-content:center;gap:10px;color:var(--white)}
  .cover-band .script{font-family:"Pinyon Script",cursive;font-size:34px}
  .cover-band .caps{font-size:24px;font-weight:500;letter-spacing:.5px}
  .cover-url{position:absolute;left:0;top:478px;width:900px;height:30px;display:flex;align-items:center;justify-content:center;
    font-size:12px;letter-spacing:5px;color:#444}

  /* Inner page */
  .inner{left:230px;top:1088px;background:var(--white)}
  .inner-panel{position:absolute;left:0;top:0;width:650px;height:440px;background:var(--blue-deep);padding:30px 26px}
  .inner-title{color:var(--white);font-size:30px;font-weight:500}
  .inner-title-rule{margin-top:14px;border-top:1px dashed var(--blue-soft)}
  .features{display:grid;grid-template-columns:1fr 1fr;column-gap:30px;row-gap:24px;margin-top:22px}
  .feature{display:flex;gap:14px;align-items:flex-start}
  .feature-icon{flex:0 0 44px;width:44px;height:44px}
  .feature p{color:var(--white);font-size:12px;line-height:1.5}
  .inner-bottom-rule{position:absolute;left:26px;right:26px;bottom:22px;border-top:1px dashed var(--blue-soft)}
  .inner-photo{position:absolute;left:650px;top:0;width:250px;height:440px;
    background:linear-gradient(100deg,#e6e6e6 0%,#bdbdbd 45%,#8a8a8a 75%,#5e5e5e 100%)}
  .inner-footer{position:absolute;left:0;top:440px;width:900px;height:68px;display:flex;align-items:center;justify-content:center;
    padding:0 20px;font-size:12px;color:var(--ink);border-top:3px solid var(--blue-pale);white-space:nowrap}

  /* Back page */
  .back{left:150px;top:1876px;background:var(--blue-deep)}
  .back-panel{position:absolute;left:0;top:0;width:630px;height:508px;
    background:radial-gradient(ellipse at 30% 40%,var(--blue-mid) 0%,var(--blue-deep) 60%,#003f84 100%)}
  .map-frame{position:absolute;left:130px;top:68px;width:380px;height:178px;border:2px solid var(--blue-pale);border-radius:18px;padding:10px}
  .map-area{width:100%;height:100%;border-radius:10px;background:linear-gradient(135deg,#eef2f4 0%,#dfe8e6 45%,#cfe0ef 70%,#b8cfe6 100%)}
  .contact{position:absolute;color:var(--white);display:flex;align-items:center;gap:10px}
  .contact svg{flex:0 0 auto}
  .contact-phone{left:165px;top:300px;font-size:28px;font-weight:500}
  .contact-address{left:165px;top:352px;font-size:15px;line-height:1.4}
  .contact-row{position:absolute;left:140px;top:444px;display:flex;gap:26px}
  .contact-row .contact{position:static;font-size:14px}
  .back-side{position:absolute;left:630px;top:0;width:270px;height:508px;
    background:linear-gradient(90deg,#f4f4f4 0%,#dedede 50%,#f6f6f6 100%)}
  .back-brand{position:absolute;left:135px;top:254px;transform:translate(-50%,-50%) rotate(-90deg);
    font-size:50px;font-weight:700;color:var(--blue-deep);white-space:nowrap}
</style>
</head>
<body>

  <!-- Cover page -->
  <section class="page cover">
    <div class="cover-brand">Harbor Wealth</div>
    <div class="cover-photo" role="img" aria-label="Photo of a suspension bridge in front of a city skyline at dusk, reflected in the river"></div>
    <div class="cover-rule"></div>
    <div class="cover-band">
      <span class="script">Are you considering</span>
      <span class="caps">ALL YOUR OPTIONS?</span>
    </div>
    <div class="cover-url">www.harborwealth.example</div>
  </section>
  <div class="page-label" style="left:1115px;top:808px;transform:rotate(-90deg)">COVER PAGE</div>

  <!-- Inner page 1 -->
  <div class="page-label" style="left:85px;top:1610px;transform:rotate(-90deg)">INNER PAGE 1</div>
  <section class="page inner">
    <div class="inner-panel">
      <h2 class="inner-title">Harbor Wealth Relationship</h2>
      <div class="inner-title-rule"></div>
      <div class="features">
        <div class="feature">
          <svg class="feature-icon" viewBox="0 0 44 44" fill="none" stroke="#fff" stroke-width="1.6"><circle cx="22" cy="22" r="20"/><path d="M15 27l5-5 4 3 6-8"/><path d="M27 17h3v3"/></svg>
          <p>Providing the highest level of wealth advisory services.</p>
        </div>
        <div class="feature">
          <svg class="feature-icon" viewBox="0 0 44 44" fill="none" stroke="#fff" stroke-width="1.6"><circle cx="22" cy="22" r="20"/><path d="M14 23l5 5 11-12"/></svg>
          <p>We love being a trusted advisor to deliver exceptional service.</p>
        </div>
        <div class="feature">
          <svg class="feature-icon" viewBox="0 0 44 44" fill="none" stroke="#fff" stroke-width="1.6"><circle cx="22" cy="22" r="20"/><rect x="14" y="14" width="16" height="16" rx="2"/><path d="M14 20h16M20 14v16"/></svg>
          <p>There are so many financial decisions that impact multiple areas of an individual's balance sheet exposing you to a potentially costly mistake.</p>
        </div>
        <div class="feature">
          <svg class="feature-icon" viewBox="0 0 44 44" fill="none" stroke="#fff" stroke-width="1.6"><circle cx="22" cy="22" r="20"/><circle cx="22" cy="22" r="9"/><circle cx="22" cy="22" r="3"/><path d="M22 22l10-10"/></svg>
          <p>Our goal is to give you the peace of mind that all aspects of your financial picture are being taken care of.</p>
        </div>
        <div class="feature">
          <svg class="feature-icon" viewBox="0 0 44 44" fill="none" stroke="#fff" stroke-width="1.6"><circle cx="22" cy="22" r="20"/><path d="M22 12v20M15 16h14M15 16l-3 8h6zM29 16l-3 8h6z"/></svg>
          <p>As an independent Registered Investment Advisor, we follow the highest financial standards.</p>
        </div>
        <div class="feature">
          <svg class="feature-icon" viewBox="0 0 44 44" fill="none" stroke="#fff" stroke-width="1.6"><circle cx="22" cy="22" r="20"/><circle cx="22" cy="22" r="9"/><path d="M22 17v10M19 19.5h5a2 2 0 010 4h-4a2 2 0 000 4h5"/></svg>
          <p>We work on a fee-only basis and do not sell commission-based or proprietary products or receive kick backs of any kind.</p>
        </div>
      </div>
      <div class="inner-bottom-rule"></div>
    </div>
    <div class="inner-photo" role="img" aria-label="Black and white photo of a light bulb standing beside stacks of coins"></div>
    <p class="inner-footer">This gives us the freedom to develop your financial plan and investment strategy without biased outside influences.</p>
  </section>

  <!-- Back page -->
  <section class="page back">
    <div class="back-panel">
      <div class="map-frame">
        <div class="map-area" role="img" aria-label="Street map showing the office location"></div>
      </div>
      <div class="contact contact-phone">
        <svg width="28" height="28" viewBox="0 0 24 24" fill="#fff"><path d="M6.6 10.8a15.1 15.1 0 006.6 6.6l2.2-2.2a1 1 0 011-.25 11.4 11.4 0 003.6.58 1 1 0 011 1V20a1 1 0 01-1 1A17 17 0 013 4a1 1 0 011-1h3.5a1 1 0 011 1c0 1.250.2 2.450.57 3.57a1 1 0 01-.25 1z"/></svg>
        <span>(555) 014-2277</span>
      </div>
      <div class="contact contact-address">
        <svg width="26" height="30" viewBox="0 0 24 28" fill="none" stroke="#fff" stroke-width="2"><path d="M12 26s8-8.5 8-15a8 8 0 10-16 0c0 6.5 8 15 8 15z"/><circle cx="12" cy="11" r="3"/></svg>
        <span>48 Alder Avenue, Suite 210<br>Riverton, WA 98001</span>
      </div>
      <div class="contact-row">
        <div class="contact">
          <svg width="26" height="24" viewBox="0 0 26 24" fill="none" stroke="#fff" stroke-width="1.8"><rect x="6" y="2" width="14" height="7"/><rect x="2" y="9" width="22" height="9" rx="2"/><rect x="6" y="14" width="14" height="8"/></svg>
          <span>(555) 014-2277</span>
        </div>
        <div class="contact">
          <svg width="26" height="26" viewBox="0 0 24 24" fill="none" stroke="#fff" stroke-width="1.6"><circle cx="12" cy="12" r="10"/><ellipse cx="12" cy="12" rx="4.5" ry="10"/><path d="M2 12h20M4 6.5h16M4 17.5h16"/></svg>
          <span>www.harborwealth.example</span>
        </div>
      </div>
    </div>
    <div class="back-side">
      <div class="back-brand">Harbor Wealth</div>
    </div>
  </section>
  <div class="page-label" style="left:1075px;top:2384px;transform:rotate(-90deg)">BACK PAGE</div>

</body>
</html>
```